PLOR-Increasing Social Capital

The attached white paper is a research planning grant proposal. I would like to take the key elements and make a pwrpt presentation to be used at an upcoming conference. Can you digest the paper and create me a summary using my TB7UM color designs but use the content from the research paper. If you have questions let me know.

Social

```html
<!DOCTYPE html>
<html lang="en">
<head>
<meta charset="utf-8">
<title>PLOR – Increasing Social Capital</title>
<link href="https://fonts.googleapis.com/css2?family=Open+Sans:wght@300;400;600;700&family=Montserrat:wght@600;700&display=swap" rel="stylesheet">
<style>
:root{
  --blue:#1a9ad6;
  --cover:#1ba6e3;
  --green:#1fae5b;
  --lime:#a5c94a;
  --teal:#19b3a8;
  --yellow:#f2c21b;
  --orange:#e2542a;
  --slate:#5b6a80;
  --ink:#222;
  --grey:#777;
  --sheet:#e2e2e2;
  --cream:#eef0dc;
}
*{box-sizing:border-box;margin:0;padding:0}
html,body{width:1200px;height:912px;overflow:hidden;background:var(--sheet);font-family:"Open Sans",Arial,sans-serif;color:var(--ink)}
.deck{position:relative;width:1200px;height:912px}
.slide{position:absolute;width:394px;height:221px;background:#fff;overflow:hidden}
.slide::before{content:"";position:absolute;left:0;top:0;bottom:0;width:9px;background:linear-gradient(90deg,var(--blue) 0 6px,var(--lime) 6px 9px)}
.c1{left:6px}.c2{left:403px}.c3{left:800px}
.r1{top:6px}.r2{top:231px}.r3{top:456px}.r4{top:681px}
.title{position:absolute;left:28px;top:14px;font-family:"Montserrat",sans-serif;font-weight:700;font-size:12.5px;color:var(--ink)}
.title span{color:var(--blue)}
.brand{position:absolute;right:18px;top:13px;display:flex;align-items:center;gap:3px;font-weight:700;font-size:9px;color:var(--blue)}
.brand i{display:block;width:9px;height:9px;border:1.2px solid var(--blue);border-radius:50%}
.rule{position:absolute;left:28px;right:18px;top:31px;height:1px;background:#f0e2a8}
.pg{position:absolute;right:6px;bottom:6px;width:13px;height:13px;background:var(--blue);color:#fff;font-size:5px;display:flex;align-items:center;justify-content:center}
.small{font-size:5px;line-height:1.45;color:var(--grey)}
.cols3{position:absolute;left:28px;right:18px;display:grid;grid-template-columns:repeat(3,1fr);gap:8px;text-align:justify}
ul.arrows{list-style:none}
ul.arrows li{position:relative;padding-left:10px}
ul.arrows li::before{content:"↗";position:absolute;left:0;color:var(--green);font-size:5px}

/* cover */
.cover{background:var(--cover)}
.cover::before{display:none}
.cover .photo{position:absolute;left:185px;top:0;width:209px;height:221px;clip-path:polygon(55px 0,100% 0,100% 100%,0 100%);background:linear-gradient(135deg,#7fa05a,#c9b08a 55%,#e7cdb4)}
.cover .cut{position:absolute;left:0;top:0;width:394px;height:221px}
.cover .name{position:absolute;left:28px;top:56px;width:62px;height:42px;border:1.5px solid #fff;border-radius:50%;display:flex;align-items:center;justify-content:center;color:#fff;font-weight:700;font-size:13px}
.cover h1{position:absolute;left:28px;top:116px;font-weight:300;font-size:15.5px;line-height:1.15;color:#fff}
.cover h1 b{font-weight:700}
.cover .sub{position:absolute;left:28px;top:165px;width:205px;font-size:6px;color:#e9f6fd;border-top:1px solid #fff;padding-top:4px;line-height:1.4}
.cover .by{position:absolute;left:28px;top:198px;font-size:5px;color:#fff}

.goals-box{position:absolute;left:28px;right:18px;top:80px;height:86px;background:#f2f2f2}
.quote{position:absolute;left:40px;right:40px;top:52px;text-align:center}
.quote .mark{font-family:"Montserrat",sans-serif;font-size:36px;color:var(--green);line-height:.8;font-weight:700}
.quote p{font-size:11px;line-height:1.35;color:#333;font-weight:300;margin-top:6px}
.quote p span{color:var(--blue)}

.eic{position:absolute;left:28px;right:30px;top:94px;height:88px;display:grid;grid-template-columns:repeat(3,1fr);gap:2px}
.eic div{position:relative;padding:20px 5px 4px;font-size:4.6px;line-height:1.4;color:#eef}
.eic b{position:absolute;left:6px;top:-4px;background:var(--yellow);color:#fff;font-size:5px;padding:2px 4px;font-weight:400}

.sample{position:absolute;left:28px;right:18px;top:72px;height:108px;display:grid;grid-template-columns:repeat(5,1fr);gap:1px;background:#fff;border-top:1px solid #ececd8}
.sample div{background:var(--cream);font-size:4.7px;line-height:1.35;text-align:center;padding:0 3px;color:#555}
.sample div b{display:block;background:#fff;color:var(--orange);font-weight:400;font-size:6px;padding:2px 0 4px;border-bottom:1px solid #f1e3a0;margin:0 -3px 4px}
.sample div:nth-child(3) b{color:var(--lime)}
.sample div:nth-child(4) b{color:var(--green)}
.sample div:nth-child(5) b{color:var(--blue)}

.table{position:absolute;left:28px;right:18px;top:74px;height:84px;border:1px solid #ddd;font-size:4.8px;color:#666}
.table .head{display:grid;grid-template-columns:1fr 1fr;background:var(--blue);color:#fff;font-size:6px;padding:1px 2px}
.table .body{display:grid;grid-template-columns:1fr 1fr;padding:2px}
.table li{border-bottom:1px solid #eee;padding:1.5px 0 1.5px 14px;list-style:none;position:relative}
.table li::before{content:"↗";position:absolute;left:4px;color:var(--yellow)}

.rising-col{position:absolute;top:42px;width:68px}
.rising-col .item{margin-bottom:6px}
.rising-col .n{font-weight:700;font-size:10px;line-height:1}
.rising-col .h{font-size:4.8px;color:var(--yellow);margin:1px 0}
.rising-col .t{font-size:3.6px;line-height:1.3;color:#aaa}

.questions{position:absolute;left:160px;right:22px;top:55px;font-size:5.6px;color:#444;line-height:1.35}
.questions li{list-style:none;position:relative;padding:0 0 3px 10px;border-bottom:1px solid #ddd;margin-bottom:3px}
.questions li::before{content:"▸";position:absolute;left:0;color:var(--yellow)}
.steps{position:absolute;top:128px;font-size:5.4px;color:#444;line-height:1.3}
.steps li{list-style:none;padding-left:9px;position:relative}
.steps li::before{content:"▸";position:absolute;left:0;color:var(--yellow)}
</style>
</head>
<body>
<main class="deck">

<!-- 1 cover -->
<section class="slide cover c1 r1">
  <div class="photo" role="img" aria-label="Photo of children learning together outdoors"></div>
  <svg class="cut" viewBox="0 0 394 221"><line x1="240" y1="0" x2="185" y2="221" stroke="#fff" stroke-width="3"/></svg>
  <div class="name">PLOR</div>
  <h1>INCREASING SOCIAL<br>CAPITAL IN <b>APPALACHIA</b></h1>
  <p class="sub">Developing an understanding of what conditions are necessary for student agency to have an impact on community vitality</p>
  <p class="by">Presented by: Sam Lee</p>
</section>

<!-- 2 executive summary -->
<section class="slide c2 r1">
  <h2 class="title">Executive <span>Summary</span></h2>
  <div class="brand"><i></i>PLOR</div><div class="rule"></div>
  <p class="small" style="position:absolute;left:28px;right:18px;top:42px;color:#555">In the spring of 2017, <b>Bright Path Institute</b>, along with the <b>Harlow Foundation</b>, sponsored a planning grant to research the nature of education innovation clusters (EICs). The research was aimed at addressing the goals and the mission of EICs and broaden the understanding of the nature of EdClusters. Specific systemic goals were identified up front.</p>
  <div class="goals-box">
    <svg style="position:absolute;left:22px;top:28px" width="34" height="34" viewBox="0 0 34 34" fill="none" stroke="#bbb" stroke-width="1"><circle cx="17" cy="15" r="7"/><path d="M14 22h6v4h-6zM17 3v3M6 8l2 2M28 8l-2 2M3 15h3M31 15h-3"/></svg>
    <ul class="arrows small" style="position:absolute;left:92px;top:6px;color:#444">
      <li>Nature and strength of the local EdCluster network</li>
      <li>EdCluster participants: their affiliations, access, levels of participation, motivations, etc.</li>
      <li>Sustainability of your EdCluster</li>
      <li>Functioning, organization, governance of your EdCluster</li>
      <li>How decision making is conducted and consensus is reached within your EdCluster</li>
      <li>How work is approached, coordinated, or prioritized across your EdCluster</li>
      <li>Nature of communications within your EdCluster network</li>
      <li>How innovation is shared and diffused within your EdCluster network</li>
    </ul>
  </div>
  <p class="small" style="position:absolute;left:28px;right:18px;top:174px;color:#555">The planning grant allowed the EIC in the <b>Plains Valley Learning Cooperative (PLOR)</b> to work with its staff and create a plan to evaluate the innovation models and the impact they have on increasing social capital. Moreover, PLOR pushed itself in the planning process to develop a deep understanding of what conditions are necessary for student agency to have an impact on vitality.</p>
  <div class="pg">2</div>
</section>

<!-- 3 introduction -->
<section class="slide c3 r1">
  <h2 class="title">Introduction</h2>
  <div class="brand"><i></i>PLOR</div><div class="rule"></div>
  <p class="small" style="position:absolute;left:28px;right:18px;top:42px;text-align:justify">Fifty three years ago, President Hale famously declared war on poverty while visiting the region. In his declaration, he stated, "I have called for a national war on poverty. Our objective: total victory." His vision was clear at the time: if this war was to be won, the mountains had to be considered ground zero, home to the poorest of the poor. Some fifty years later, the results are mixed, with communities still struggling toward prosperity. The Appalachian region itself is home to over twenty five million people and covers parts of mostly mountainous areas of 13 states, stretching from the southern highlands to the northern ridges and the whole of one state.</p>
  <div class="cols3 small" style="top:110px">
    <p>Parts of Appalachia are characterized by the rugged topography that puts the region at a disadvantage because of the transportation and infrastructure problems that have developed over time. Through most of the region there is a barrage of issues ranging from inadequate jobs, services, transportation, education, and its isolation from growth centers. These factors are compounded in education and certainly have an</p>
    <p>impact on education outcomes. By failing to account for the out-of-school class factors that affect student achievement, reproduction of social inequality in the schools' education systems produce a systemic problem that has existed for years and even decades. Studying the role of school factors, researchers discovered that the relationships and networks between and among people that help guide behavior, norms, and values were contributing factors to social</p>
    <p>reproduction in the form of social capital. This research, popularly known as a landmark report, showed that once students' academic and family backgrounds were taken into consideration, the characteristics of schools accounted for very few variations in students' achievement. The social capital within the schools and whether students could benefit from their parents and communities all had greater impacts on learning.</p>
  </div>
  <div class="pg">3</div>
</section>

<!-- 4 introduction 2 -->
<section class="slide c1 r2">
  <h2 class="title">Introduction</h2>
  <div class="brand"><i></i>PLOR</div><div class="rule"></div>
  <div class="cols3 small" style="top:58px">
    <p>Researchers went on to define social capital as the "benefits that come from social organizations such as networking, societal norms, and a generalized trust, which lead to cooperation and progress." The early report began to establish that family background and socioeconomic conditions accounted for most of the achievement gap along socio economic populations. Additional research concluded that within the school environment, schools contribute up to one-third of a student's achievement and outcomes while family and community characteristics contribute two-</p>
    <p>thirds. This is especially true in Appalachia where generations of poverty have existed. Yet despite all the challenges and struggles faced by Appalachians, there are sea beds of hope that may very well light the way for others to follow. Embedded in the eastern part of the region is the Plains Valley Learning Cooperative (PLOR) that has taken up the call to change the social capital for the region. PLOR realized early on that it should not only focus on the social and economic divisions within the region but also battle the often incorrect and over-generalizations about the region. To focus all its energy and solutions toward this, PLOR developed a</p>
    <p>system of supports that are levered by the communities and involve a wide range of constituents. Throughout the process PLOR looked for solutions that were developed internal to the region, ones that not only could have an impact but had the potential to scale across communities. At the center of the PLOR model is teaching, leadership, and learning. PLOR's goal is to create levers for all its resources that have the potential to create a lasting impact through education innovations. The efforts of PLOR have not remain unnoticed and recently the region was awarded the designation of being an Education Innovation Cluster or EIC.</p>
  </div>
  <div class="pg">4</div>
</section>

<!-- 5 EIC -->
<section class="slide c2 r2">
  <h2 class="title">Education Innovation <span>Clusters</span></h2>
  <div class="brand"><i></i>PLOR</div><div class="rule"></div>
  <p class="small" style="position:absolute;left:28px;right:18px;top:52px;font-size:5.6px">Education Innovation Clusters (EIC) are geographic concentrations of organizations, institutions, and thought leaders working together to develop and nurture educational technologies and exceptional learning practices.</p>
  <div class="eic">
    <div style="background:var(--slate)"><b>01</b>Educational partners (early learning providers, schools, libraries, community centers, afterschool programs, postsecondary education programs and institutions, and virtual learning) support the environment where emerging learning technologies can be piloted and new solutions developed with input from students and teachers.</div>
    <div style="background:var(--blue)"><b>02</b>Research partners conduct advance the field of learning practices to advance the field of learning science. They are fully integrated with entrepreneurial partners for learning technology design, and linked closely with educational partners for data and outcomes to feed evaluations of new approaches.</div>
    <div style="background:var(--green)"><b>03</b>Commercial partners scale and market successful implementations, providing investment capital for acceleration of commercialization.</div>
  </div>
  <div class="pg">5</div>
</section>

<!-- 6 Appalachia Rising -->
<section class="slide c3 r2">
  <h2 class="title">Appalachia <span>Rising</span></h2>
  <div class="brand"><i></i>PLOR</div><div class="rule"></div>
  <div class="rising-col" style="left:28px">
    <div class="item"><div class="n">01</div><div class="h">HEADER YOUR TEXT</div><div class="t">Developing an understanding of what conditions are necessary for student agency to have an impact on vitality.</div></div>
    <div class="item"><div class="n">02</div><div class="h">HEADER YOUR TEXT</div><div class="t">Developing an understanding of what conditions are necessary for student agency to have an impact on vitality.</div></div>
    <div class="item"><div class="n">03</div><div class="h">HEADER YOUR TEXT</div><div class="t">Developing an understanding of what conditions are necessary for student agency to have an impact on vitality.</div></div>
    <div class="item"><div class="n">04</div><div class="h">HEADER YOUR TEXT</div><div class="t">Developing an understanding of what conditions are necessary for student agency to have an impact on vitality.</div></div>
  </div>
  <div class="rising-col" style="left:302px">
    <div class="item"><div class="n">05</div><div class="h">HEADER YOUR TEXT</div><div class="t">Developing an understanding of what conditions are necessary for student agency to have an impact on vitality.</div></div>
    <div class="item"><div class="n">06</div><div class="h">HEADER YOUR TEXT</div><div class="t">Developing an understanding of what conditions are necessary for student agency to have an impact on vitality.</div></div>
    <div class="item"><div class="n">07</div><div class="h">HEADER YOUR TEXT</div><div class="t">Developing an understanding of what conditions are necessary for student agency to have an impact on vitality.</div></div>
    <div class="item"><div class="n">08</div><div class="h">HEADER YOUR TEXT</div><div class="t">Developing an understanding of what conditions are necessary for student agency to have an impact on vitality.</div></div>
  </div>
  <svg style="position:absolute;left:100px;top:34px" width="196" height="182" viewBox="0 0 196 182" font-family="Open Sans,sans-serif" font-size="4.2" fill="#fff" text-anchor="middle">
    <g fill="var(--yellow)">
      <polygon points="98,50 93,56 103,56"/><polygon points="98,132 93,126 103,126"/>
      <polygon points="57,91 63,86 63,96"/><polygon points="139,91 133,86 133,96"/>
    </g>
    <g fill="var(--green)"><polygon points="70,62 74,70 66,68"/><polygon points="126,120 122,112 130,114"/></g>
    <g fill="var(--blue)"><polygon points="126,62 122,70 130,68"/><polygon points="70,120 74,112 66,114"/></g>
    <circle cx="98" cy="91" r="30" fill="var(--orange)"/>
    <text x="98" y="84">What are the key</text><text x="98" y="89">elements to rewriting</text><text x="98" y="94">the education</text><text x="98" y="99">narrative in</text><text x="98" y="104">Appalachia?</text>
    <circle cx="98" cy="26" r="19" fill="var(--yellow)"/><text x="98" y="25">EDUCATION</text><text x="98" y="30">AND WORK</text>
    <circle cx="144" cy="44" r="19" fill="var(--lime)"/><text x="144" y="43">SCHOOL &amp;</text><text x="144" y="48">COMMUNITY</text>
    <circle cx="164" cy="91" r="19" fill="var(--green)"/><text x="164" y="93">LEADERSHIP</text>
    <circle cx="144" cy="138" r="19" fill="var(--blue)"/><text x="144" y="137">TECHNOLOGY</text><text x="144" y="142">&amp; INNOVATION</text>
    <circle cx="98" cy="156" r="19" fill="var(--slate)"/><text x="98" y="155">EDUCATION</text><text x="98" y="160">TALENT</text>
    <circle cx="52" cy="138" r="19" fill="var(--yellow)"/><text x="52" y="137">DATA</text><text x="52" y="142">ANALYSIS</text>
    <circle cx="32" cy="91" r="19" fill="var(--lime)"/><text x="32" y="90">STUDENT</text><text x="32" y="95">AGENCY</text>
    <circle cx="52" cy="44" r="19" fill="var(--green)"/><text x="52" y="43">READINESS /</text><text x="52" y="48">WELLNESS</text>
  </svg>
  <div class="pg">6</div>
</section>

<!-- 7 research questions -->
<section class="slide c1 r3">
  <h2 class="title">Research <span>Questions</span></h2>
  <div class="brand"><i></i>PLOR</div><div class="rule"></div>
  <svg style="position:absolute;left:30px;top:62px" width="130" height="124" viewBox="0 0 130 124">
    <polygon points="40,62 128,0 128,124" fill="var(--blue)"/>
    <circle cx="40" cy="62" r="26" fill="#1769b0"/>
    <text x="40" y="73" text-anchor="middle" font-family="Montserrat,sans-serif" font-weight="700" font-size="32" fill="#fff">?</text>
  </svg>
  <ul class="questions">
    <li>What conditions are necessary for student agency to lever community social capital investment in advancing community vitality?</li>
    <li>How is student agency operating in these cases?</li>
    <li>What does student agency look like in these case studies?</li>
    <li>What conditions were necessary and what were the enabling conditions in these models?</li>
    <li>How do the key stakeholders perceive the resources? How are the resources being used?</li>
    <li>What additional resources might be needed for an additional outcome?</li>
    <li>Where are there pockets of productive activity in these cases?</li>
  </ul>
  <div class="pg">7</div>
</section>

<!-- 8 research goals -->
<section class="slide c2 r3">
  <h2 class="title">Research <span>Goals</span></h2>
  <div class="brand"><i></i>PLOR</div><div class="rule"></div>
  <div class="quote">
    <div class="mark">”</div>
    <p>The research <span>being proposed offers</span> the PLOR innovation cluster the opportunity to develop a deeper understanding of the resources available, away to apply those resources to connect to community development, and an overall strategy to improve the economic, education, and employment viability of the region.</p>
  </div>
  <div class="pg">8</div>
</section>

<!-- 9 research sample -->
<section class="slide c3 r3">
  <h2 class="title">Research <span>Sample</span></h2>
  <div class="brand"><i></i>PLOR</div><div class="rule"></div>
  <p style="position:absolute;left:28px;top:42px;font-size:7.6px;color:#444">The five broad interconnected components of EL</p>
  <div class="sample">
    <div><b>01</b>Developing effective elementary Principals and teachers with a specific focus on the elementary Principal as the lead learner,</div>
    <div><b>02</b>Professional Action Networks (PANs) of practitioners focused on community engagement and balanced assessment of learning,</div>
    <div><b>03</b>Social network Mapping Project to increase human capital investment in learning,</div>
    <div><b>04</b>Concentrated community and caregiver training and engagement process,</div>
    <div><b>05</b>Development of a digital School/Community Resource Matrix that services to firmly connect the school and the community to learning targets and focuses on matching need to available resources.</div>
  </div>
  <div class="pg">9</div>
</section>

<!-- 10 sampling process -->
<section class="slide c1 r4">
  <h2 class="title">Sampling <span>Process</span></h2>
  <div class="brand"><i></i>PLOR</div><div class="rule"></div>
  <svg style="position:absolute;left:28px;top:56px" width="352" height="56" viewBox="0 0 352 56" font-family="Open Sans,sans-serif" font-size="8.6" fill="#fff" text-anchor="middle">
    <polygon points="0,0 116,0 134,28 116,56 0,56" fill="var(--green)"/>
    <polygon points="112,0 232,0 250,28 232,56 112,56 130,28" fill="var(--teal)"/>
    <polygon points="228,0 334,0 352,28 334,56 228,56 246,28" fill="var(--blue)"/>
    <polyline points="116,0 134,28 116,56" fill="none" stroke="#fff" stroke-width="2"/>
    <polyline points="232,0 250,28 232,56" fill="none" stroke="#fff" stroke-width="2"/>
    <text x="62" y="25">EL3 Schools (13 identified</text><text x="62" y="36">schools)</text>
    <text x="184" y="25">EL3 Exemplary (4)</text><text x="184" y="36">Case Studies</text>
    <text x="296" y="25">Published Models</text><text x="296" y="36">of the EL3 Schools</text>
  </svg>
  <ul class="steps" style="left:38px"><li>6 Elementary Schools</li><li>2 Middle Schools</li><li>5 High Schools</li></ul>
  <ul class="steps" style="left:152px;border-left:1px dashed #ccc;padding-left:6px"><li>2 Elementary Schools</li><li>1 Middle School</li><li>1 High School</li></ul>
  <ul class="steps" style="left:254px;width:110px;border-left:1px dashed #ccc;padding-left:6px"><li>Developing effective Principals and teachers</li><li>Professional Action Networks (PANs)</li><li>Social network Mapping</li><li>Concentrated community and caregiver training</li><li>Development of a digital School/Community Resource Matrix</li></ul>
  <div class="pg">10</div>
</section>

<!-- 11 data sources -->
<section class="slide c2 r4">
  <h2 class="title">Data <span>Sources</span></h2>
  <div class="brand"><i></i>PLOR</div><div class="rule"></div>
  <div class="table">
    <div class="head"><span>QUANTITATIVE</span><span>QUALITATIVE</span></div>
    <div class="body">
      <ul><li>School Report Cards</li><li>Teacher Evaluation Data</li><li>Existence of community Projects that extend beyond school</li><li>Student Lead Projects as demonstrated</li><li>Student Performance and Attendance</li><li>Community Attendance at Project Demonstrations</li><li>Community review and participation of students led projects</li></ul>
      <ul><li>Student Interviews</li><li>Teacher Interviews</li><li>Community Participation List</li><li>Social Network Map-How was it Developed</li><li>Social Network Map-Who Participated</li><li>Professional Development Participation</li><li>Access to the asset maps</li></ul>
    </div>
  </div>
  <div class="pg">11</div>
</section>

<!-- 12 research impact -->
<section class="slide c3 r4">
  <h2 class="title">Research <span>Impact</span></h2>
  <div class="brand"><i></i>PLOR</div><div class="rule"></div>
  <svg style="position:absolute;left:107px;top:36px" width="180" height="180" viewBox="0 0 180 180" font-family="Open Sans,sans-serif" font-size="5.2" fill="#fff" text-anchor="middle">
    <g fill="var(--green)"><polygon points="90,50 85,44 95,44"/><polygon points="90,112 85,118 95,118"/></g>
    <g fill="var(--teal)"><polygon points="118,70 124,63 126,72"/><polygon points="62,70 56,63 54,72"/><polygon points="118,94 124,100 126,91"/><polygon points="62,94 56,100 54,91"/></g>
    <circle cx="90" cy="81" r="24" fill="var(--lime)"/>
    <text x="90" y="79" font-size="9">Social</text><text x="90" y="90" font-size="9">Capital</text>
    <circle cx="90" cy="23" r="22" fill="var(--green)"/><text x="90" y="22">Rural</text><text x="90" y="29">Education</text>
    <circle cx="140" cy="52" r="22" fill="var(--green)"/><text x="140" y="48">Education /</text><text x="140" y="55">Administrati</text><text x="140" y="62">on</text>
    <circle cx="140" cy="112" r="22" fill="var(--teal)"/><text x="140" y="111">Place Based</text><text x="140" y="118">Models</text>
    <circle cx="90" cy="142" r="22" fill="var(--teal)"/><text x="90" y="141">Organizatio</text><text x="90" y="148">nal Change</text>
    <circle cx="40" cy="112" r="22" fill="var(--blue)"/><text x="40" y="111">Decision</text><text x="40" y="118">Making</text>
    <circle cx="40" cy="52" r="22" fill="var(--blue)"/><text x="40" y="51">Professional</text><text x="40" y="58">Practice</text>
  </svg>
  <div class="pg">12</div>
</section>

</main>
</body>
</html>
```